Design for Card Attached to Clothes

We sell rhythmic gymnastics apparel and are looking for someone create a card that will be attached to the products. You can see an example of the exact type of apparel in the files, as well as the current card that is attached to it. The design should have space on the top back for the sticker that has UPC and SKU information, as shown in the image attached.
- We would like the front to have our logo
- We would like the image of the girls added on the back
- Would be cool to see the gradient change to the white space on the back where the sticker will go but not required.
-The final card size is 10cm by 6cm, Their should be 2mm loss accounted for cutting the cards within the design. (meaning the design needs to be bigger than 10cm by 6cm to account for printing and cut)
- And the hole size that is at the top center is 3mm in diameter
- Name should be under logo
Access all logo files here https://files.plomvarek.net/share/folders/7Kq2TzWm9RbXa4LpYc8NdVe3Hs5JfGu1?view=open
- Front will have logo
- Back will have image of girls and some creative design that you will create.
Females
Rhythmic Gymnastics

```html
<!DOCTYPE html>
<html lang="en">
<head>
<meta charset="utf-8">
<title>Velmora hang tag – front and back</title>
<link rel="stylesheet" href="https://fonts.googleapis.com/css2?family=Poppins:wght@400;500&family=Pinyon+Script&display=swap">
<style>
  :root {
    --stage: #3a3a3a;
    --paper: #ffffff;
    --magenta: #e90b78;
    --violet: #a8329e;
    --outfit: #1e1b1d;
    --ink: #1c1c1c;
    --sans: "Poppins", Arial, sans-serif;
    --script: "Pinyon Script", cursive;
  }
  * { box-sizing: border-box; margin: 0; padding: 0; }
  html, body { width: 1200px; height: 1200px; overflow: hidden; }
  body { background: var(--stage); position: relative; font-family: var(--sans); }

  .tag {
    position: absolute;
    top: 250px;
    width: 420px;
    height: 700px;
    background: var(--paper);
  }
  .tag--front { left: 150px; }
  .tag--back  { left: 630px; }

  /* front */
  .tag__panel {
    position: absolute;
    inset: 22px;
    border-radius: 14px;
    background: linear-gradient(225deg, var(--magenta) 0%, var(--magenta) 45%, var(--violet) 100%);
  }
  .tag__hole {
    position: absolute;
    left: 50%;
    width: 22px;
    height: 22px;
    margin-left: -11px;
    border-radius: 50%;
  }
  .tag__panel .tag__hole { top: 30px; background: var(--paper); }
  .brand-mark {
    position: absolute;
    left: 50%;
    top: 150px;
    width: 196px;
    height: 196px;
    margin-left: -98px;
    border-radius: 50%;
    background: var(--paper);
  }
  .brand-name {
    position: absolute;
    left: 0; right: 0;
    top: 356px;
    text-align: center;
    color: var(--paper);
    font-weight: 500;
    font-size: 46px;
    line-height: 1.2;
    letter-spacing: 1px;
  }

  /* back */
  .tag--back .tag__hole {
    top: 60px;
    border: 2px solid var(--magenta);
    background: transparent;
  }
  .product-photo {
    position: absolute;
    left: 60px;
    right: 60px;
    top: 210px;
    height: 370px;
    border-radius: 8px;
    background: linear-gradient(200deg, var(--magenta) 0%, #b02a7e 40%, #4a2140 75%, var(--outfit) 100%);
  }
  .tagline {
    position: absolute;
    left: 0; right: 0;
    top: 580px;
    text-align: center;
  }
  .tagline__script {
    display: block;
    font-family: var(--script);
    font-size: 74px;
    line-height: 1;
    color: var(--magenta);
  }
  .tagline__sub {
    display: block;
    margin: -4px 0 0 110px;
    font-size: 16px;
    line-height: 1.2;
    color: var(--ink);
  }
</style>
</head>
<body>
  <section class="tag tag--front" aria-label="Tag front">
    <div class="tag__panel">
      <span class="tag__hole"></span>
      <span class="brand-mark" aria-hidden="true"></span>
      <p class="brand-name">Velmora</p>
    </div>
  </section>

  <section class="tag tag--back" aria-label="Tag back">
    <span class="tag__hole"></span>
    <div class="product-photo" role="img" aria-label="Photo of two young gymnasts in black short-sleeve leotards and leggings standing in front of a magenta backdrop"></div>
    <p class="tagline">
      <span class="tagline__script">Rhythmic</span>
      <span class="tagline__sub">gymnastics appare</span>
    </p>
  </section>
</body>
</html>
```